BEACON CABS

Taxi card design

Need changes very slow in replying to my messages.

Target Market(s)

Customers

Industry/Entity Type

Taxi

Contact Information for Business Card

See previous design

Font styles to use
Sans Serif

Colors
A7469A
B969AE
D3A5CF
EDDBEB
F8F0F9
6B429C
8869AF
B7A5CE
E3DAEB
F3F0F8

Requirements
Nice to have
• We are in the business of looking after people, not just driving vehicles front
Should not have
• Front number 01632 480 480 needs to big big

```html
<!DOCTYPE html>
<html lang="en">
<head>
<meta charset="utf-8">
<title>Beacon Cabs – Business Cards</title>
<link rel="stylesheet" href="https://fonts.googleapis.com/css2?family=Montserrat:wght@500;600;700;800&display=swap">
<style>
  :root {
    --magenta: #A7469A;
    --magenta-soft: #B969AE;
    --magenta-pale: #F8F0F9;
    --violet: #6B429C;
    --violet-soft: #8869AF;
    --ink: #2b2b2b;
    --paper: #ffffff;
    --board: #e8e8e8;
  }
  * { box-sizing: border-box; margin: 0; padding: 0; }
  html, body { width: 982px; height: 1200px; overflow: hidden; }
  body {
    position: relative;
    background: var(--board);
    font-family: "Montserrat", sans-serif;
    color: var(--ink);
  }

  /* Brand lockup (text only) */
  .brand { display: flex; flex-direction: column; align-items: center; line-height: 1; }
  .brand__service { align-self: flex-end; font-weight: 700; }
  .brand__row { display: flex; align-items: center; }
  .brand__dot { background: var(--magenta); border-radius: 50%; flex: none; }
  .brand__name { font-weight: 800; color: var(--ink); white-space: nowrap; letter-spacing: -0.01em; }
  .brand__since { align-self: flex-end; font-weight: 600; }

  .hero-brand { position: absolute; left: 0; right: 0; top: 70px; margin: 0 auto; width: 440px; }
  .hero-brand .brand__service { font-size: 21px; margin-bottom: 8px; }
  .hero-brand .brand__dot { width: 26px; height: 26px; margin-right: 14px; }
  .hero-brand .brand__name { font-size: 58px; }
  .hero-brand .brand__since { font-size: 12px; margin-top: 8px; }

  /* Cards: 1em = 1% of card width */
  .card {
    position: absolute;
    width: 100em; height: 56.9em;
    background: var(--paper);
    overflow: hidden;
  }
  .card--feature { font-size: 6.2px; left: 181px; top: 360px; box-shadow: 0 10px 30px rgba(0,0,0,.12); }
  .card--front { font-size: 3.93px; left: 80px; top: 917px; }
  .card--back  { font-size: 3.93px; left: 509px; top: 917px; }

  .card .brand { position: absolute; left: 0; right: 0; margin: 0 auto; width: 62em; }
  .card .brand__service { font-size: 3em; margin-bottom: 0.6em; }
  .card .brand__dot { width: 4.2em; height: 4.2em; margin-right: 2em; }
  .card .brand__name { font-size: 8.6em; }
  .card .brand__since { font-size: 1.9em; margin-top: 0.7em; }
  .card--front .brand, .card--feature .brand { top: 6em; }
  .card--back .brand { top: 12em; }

  .services { position: absolute; top: 26.8em; left: 4.9em; right: 5em; display: flex; gap: 2em; }
  .services__item {
    height: 6.6em; display: flex; align-items: center; justify-content: center;
    color: var(--paper); font-weight: 600; font-size: 1em; border-radius: 0.8em;
  }
  .services__item span { font-size: 3em; }
  .services__item--airport { width: 33.9em; background: var(--violet); }
  .services__item--minibus { width: 18.4em; background: var(--magenta); }
  .services__item--school { flex: 1; background: var(--violet); }

  .lines { position: absolute; top: 35.4em; left: 0; right: 0; height: 6.2em; display: flex; }
  .lines__item {
    flex: 1; display: flex; align-items: center; justify-content: center; gap: 0.8em;
    color: var(--paper); background: var(--magenta); font-weight: 600;
  }
  .lines__item--mid { background: var(--violet); border-radius: 1em 1em 0 0; }
  .lines__item span { font-size: 2.7em; letter-spacing: 0.08em; }
  .lines__item svg { width: 1.8em; height: 2.4em; }

  .details { position: absolute; top: 43.8em; left: 4.5em; right: 4.5em; display: flex; justify-content: space-between; }
  .details p { font-size: 2.4em; font-weight: 600; line-height: 1.25; }

  .pattern-strip {
    position: absolute; left: 0; right: 0; bottom: 0; height: 2.6em;
    background: linear-gradient(to bottom, var(--paper), var(--magenta-pale));
  }

  .hotline {
    position: absolute; left: 0; right: 0; top: 37.5em;
    display: flex; align-items: center; justify-content: center; gap: 1.8em;
  }
  .hotline__icon { width: 4.6em; height: 4.6em; background: var(--ink); border-radius: 0.8em; display: flex; align-items: center; justify-content: center; }
  .hotline__icon svg { width: 2.6em; height: 3em; }
  .hotline__number { font-size: 4.8em; font-weight: 700; letter-spacing: 0.28em; }
</style>
</head>
<body>

  <header class="brand hero-brand">
    <span class="brand__service">24/7 SERVICE</span>
    <div class="brand__row"><span class="brand__dot"></span><span class="brand__name">BEACON CABS</span></div>
    <span class="brand__since">Established since 1986</span>
  </header>

  <!-- Contact card, enlarged -->
  <article class="card card--feature">
    <div class="brand">
      <span class="brand__service">24/7 SERVICE</span>
      <div class="brand__row"><span class="brand__dot"></span><span class="brand__name">BEACON CABS</span></div>
      <span class="brand__since">Established since 1986</span>
    </div>
    <ul class="services">
      <li class="services__item services__item--airport"><span>AIRPORT TRANSFERS</span></li>
      <li class="services__item services__item--minibus"><span>MINIBUSES</span></li>
      <li class="services__item services__item--school"><span>SCHOOL TRANSPORT</span></li>
    </ul>
    <div class="lines">
      <div class="lines__item"><svg viewBox="0 0 12 16"><path d="M4 1 C1 2 0 5 1 9 C2 13 5 15 8 15 L9 12 L6 11 C5 10 4 7 4 5 L7 4 Z" fill="#fff"/></svg><span>01632 960 111</span></div>
      <div class="lines__item lines__item--mid"><svg viewBox="0 0 12 16"><path d="M4 1 C1 2 0 5 1 9 C2 13 5 15 8 15 L9 12 L6 11 C5 10 4 7 4 5 L7 4 Z" fill="#fff"/></svg><span>01632 960 222</span></div>
      <div class="lines__item"><svg viewBox="0 0 12 16"><path d="M4 1 C1 2 0 5 1 9 C2 13 5 15 8 15 L9 12 L6 11 C5 10 4 7 4 5 L7 4 Z" fill="#fff"/></svg><span>01632 960 333</span></div>
    </div>
    <div class="details">
      <p>Freephone: 0800 000 0 480<br>E-mail: hello@beaconcabs.example<br>Website: www.beaconcabs.example</p>
      <p>St Marys Parish Hall<br>Market Lane Northdale<br>ND4 7QA</p>
    </div>
    <div class="pattern-strip" role="img" aria-label="Faint repeating taxi pattern along the bottom edge"></div>
  </article>

  <!-- Contact card -->
  <article class="card card--front">
    <div class="brand">
      <span class="brand__service">24/7 SERVICE</span>
      <div class="brand__row"><span class="brand__dot"></span><span class="brand__name">BEACON CABS</span></div>
      <span class="brand__since">Established since 1986</span>
    </div>
    <ul class="services">
      <li class="services__item services__item--airport"><span>AIRPORT TRANSFERS</span></li>
      <li class="services__item services__item--minibus"><span>MINIBUSES</span></li>
      <li class="services__item services__item--school"><span>SCHOOL TRANSPORT</span></li>
    </ul>
    <div class="lines">
      <div class="lines__item"><svg viewBox="0 0 12 16"><path d="M4 1 C1 2 0 5 1 9 C2 13 5 15 8 15 L9 12 L6 11 C5 10 4 7 4 5 L7 4 Z" fill="#fff"/></svg><span>01632 960 111</span></div>
      <div class="lines__item lines__item--mid"><svg viewBox="0 0 12 16"><path d="M4 1 C1 2 0 5 1 9 C2 13 5 15 8 15 L9 12 L6 11 C5 10 4 7 4 5 L7 4 Z" fill="#fff"/></svg><span>01632 960 222</span></div>
      <div class="lines__item"><svg viewBox="0 0 12 16"><path d="M4 1 C1 2 0 5 1 9 C2 13 5 15 8 15 L9 12 L6 11 C5 10 4 7 4 5 L7 4 Z" fill="#fff"/></svg><span>01632 960 333</span></div>
    </div>
    <div class="details">
      <p>Freephone: 0800 000 0 480<br>E-mail: hello@beaconcabs.example<br>Website: www.beaconcabs.example</p>
      <p>St Marys Parish Hall<br>Market Lane Northdale<br>ND4 7QA</p>
    </div>
    <div class="pattern-strip" role="img" aria-label="Faint repeating taxi pattern along the bottom edge"></div>
  </article>

  <!-- Hotline card -->
  <article class="card card--back">
    <div class="brand">
      <span class="brand__service">24/7 SERVICE</span>
      <div class="brand__row"><span class="brand__dot"></span><span class="brand__name">BEACON CABS</span></div>
      <span class="brand__since">Established since 1986</span>
    </div>
    <div class="hotline">
      <span class="hotline__icon"><svg viewBox="0 0 12 16"><path d="M4 1 C1 2 0 5 1 9 C2 13 5 15 8 15 L9 12 L6 11 C5 10 4 7 4 5 L7 4 Z" fill="#fff"/></svg></span>
      <span class="hotline__number">01632 480 480</span>
    </div>
  </article>

</body>
</html>
```